EXPEDITE! Business Card For a Private Equity Firm
Fresh and Sleek
EXPEDITE!  Business Card For a Private Equity Firm - Financial Services
Creative Brief
Bright & Fun-filled
Ted Morrow
Managing Partner
782 Lindell Street New York, NY 10233
ted@vorintek-example.com
www.vorintek-example.com
Looking for a fresh look on our new business cards. We have had previous designs on Plenavox for similar companies, but, now is time to refresh the look! Please submit as many design as possible. We will give you fast, efficient feedback!
Vorintek Vorintek
All. We also need email signatures and letterhead. Please provide.

```html
<!DOCTYPE html>
<html lang="en">
<head>
<meta charset="utf-8">
<title>Vorintek Business Card</title>
<link href="https://fonts.googleapis.com/css2?family=Cinzel:wght@400;600&family=Open+Sans:wght@400&display=swap" rel="stylesheet">
<style>
  :root {
    --stage: #e9e7e3;
    --card: #ffffff;
    --brand-blue: #1f5fb0;
    --name-blue: #2a86d6;
    --ink: #2b2f36;
    --muted: #555a62;
    --rule: #b9bcc2;
    --pattern-light: #f4f8fc;
    --pattern-tone: #dfe9f4;
  }
  * { box-sizing: border-box; margin: 0; padding: 0; }
  html, body { width: 1200px; height: 900px; overflow: hidden; }
  body { background: var(--stage); position: relative; font-family: "Open Sans", sans-serif; }

  .card {
    position: absolute; left: 300px; width: 600px; height: 343px;
    border-radius: 22px; background: var(--card); overflow: hidden;
    box-shadow: 0 10px 28px rgba(0,0,0,0.18);
  }
  .card--back { top: 60px; }
  .card--front { top: 470px; }

  .back-pattern {
    position: absolute; inset: 0;
    background: linear-gradient(135deg, var(--pattern-light), var(--pattern-tone) 50%, var(--pattern-light));
  }
  .back-brand {
    position: absolute; left: 0; right: 0; top: 120px;
    display: flex; justify-content: center; align-items: center; gap: 12px;
  }
  .brand-dot { width: 26px; height: 26px; border-radius: 50%; background: var(--brand-blue); }
  .brand-name {
    font-family: "Cinzel", serif; font-weight: 600; color: var(--brand-blue);
    letter-spacing: 2px; text-transform: uppercase;
  }
  .back-brand .brand-name { font-size: 34px; }
  .back-url {
    position: absolute; left: 0; right: 0; top: 205px;
    display: flex; justify-content: center; align-items: center; gap: 10px;
    font-size: 14px; letter-spacing: 3px; color: var(--muted);
  }
  .back-url::before, .back-url::after { content: ""; width: 40px; height: 1px; background: var(--rule); }

  .front-brand {
    position: absolute; left: 0; right: 0; top: 40px;
    display: flex; justify-content: center; align-items: center; gap: 14px;
  }
  .front-brand .brand-name { font-size: 50px; }
  .front-brand .brand-dot { width: 34px; height: 34px; }

  .person { position: absolute; left: 0; right: 0; top: 132px; text-align: center; }
  .person-name { font-family: "Cinzel", serif; font-size: 26px; color: var(--name-blue); }
  .person-title {
    font-family: "Cinzel", serif; font-weight: 600; font-size: 17px; color: var(--ink);
    letter-spacing: 1px; margin-top: 2px;
  }

  .contact-row {
    position: absolute; left: 22px; right: 22px; bottom: 38px;
    display: flex; align-items: center; justify-content: space-between;
    font-size: 13.5px; color: var(--muted); line-height: 1.6;
  }
  .contact-col { display: flex; flex-direction: column; }
  .divider { width: 1px; height: 40px; background: var(--rule); }
  .contact-item { display: flex; align-items: center; gap: 7px; }
  .icon { width: 14px; height: 14px; fill: var(--brand-blue); flex-shrink: 0; }
</style>
</head>
<body>

<section class="card card--back">
  <div class="back-pattern" role="img" aria-label="Light blue repeating geometric pattern background"></div>
  <div class="back-brand">
    <span class="brand-dot"></span>
    <span class="brand-name">Vorintek</span>
  </div>
  <div class="back-url">www.vorintek-example.com</div>
</section>

<section class="card card--front">
  <div class="front-brand">
    <span class="brand-dot"></span>
    <span class="brand-name">Vorintek</span>
  </div>

  <div class="person">
    <div class="person-name">Ted Morrow</div>
    <div class="person-title">Managing Partner</div>
  </div>

  <div class="contact-row">
    <div class="contact-col address">
      <span>782 Lindell Street</span>
      <span>New York, NY 10233</span>
    </div>
    <span class="divider"></span>
    <div class="contact-col phones">
      <span class="contact-item">
        <svg class="icon" viewBox="0 0 16 16"><path d="M3 1h3l1.5 4-2 1.2a9 9 0 0 0 4.3 4.3L11 8.5l4 1.5v3a2 2 0 0 1-2 2C7 15 1 9 1 3a2 2 0 0 1 2-2z"/></svg>
        (555) 240-0120
      </span>
      <span class="contact-item">
        <svg class="icon" viewBox="0 0 16 16"><rect x="4" y="1" width="8" height="5"/><rect x="1" y="6" width="14" height="6" rx="1"/><rect x="4" y="10" width="8" height="5"/></svg>
        (555) 240-0130
      </span>
    </div>
    <span class="divider"></span>
    <div class="contact-col online">
      <span class="contact-item">
        <svg class="icon" viewBox="0 0 16 16"><path d="M1 3h14v10H1z M1 3l7 6 7-6" fill="none" stroke="#1f5fb0" stroke-width="1.6"/></svg>
        ted@vorintek-example.com
      </span>
      <span class="contact-item">
        <svg class="icon" viewBox="0 0 16 16"><circle cx="8" cy="8" r="6.5" fill="none" stroke="#1f5fb0" stroke-width="1.4"/><path d="M1.5 8h13M8 1.5c-3 3.5-3 9.5 0 13M8 1.5c3 3.5 3 9.5 0 13" fill="none" stroke="#1f5fb0" stroke-width="1.2"/></svg>
        www.vorintek-example.com
      </span>
    </div>
  </div>
</section>

</body>
</html>
```